Wedding Ceremony Equipment Hire Business Card

I need a business card design for a new business I created called Vow Outfitters. We hire out Wedding Ceremony equipment and decorations mainly for beach and garden wedding ceremonies that include delivery, set up and dismantle. We do offer DIY Chair Hire as well.
I'd like to have a similar design and colours to our website:
www.vowoutfitters-example.com.au
If possible would like the front to incorporate our information and logo and the back to have two faded example pictures of our wedding ceremonies.
I have attached two photos and our logo. Please let me know if you need a better pic of our logo though.

Target Market(s)

Newly engaged couples, aged 25 and upwards

Industry/Entity Type

Wedding

Contact Information for Business Card

Vow Outfitters
Merel Thorpe
0491 870 264
vowoutfitters@mailbox-example.com
www.social-example.com/VowOutfitters

```html
<!DOCTYPE html>
<html lang="en">
<head>
<meta charset="utf-8">
<title>Vow Outfitters – Business Card</title>
<link rel="stylesheet" href="https://fonts.googleapis.com/css2?family=Questrial&display=swap">
<style>
  :root {
    --bg: #ece8e2;
    --card-white: #ffffff;
    --card-black: #141414;
    --pattern-dark: #1f1f1f;
    --pattern-mid: #2c2c2c;
    --teal: #86d3c1;
    --ink: #1b1b1b;
    --text-light: #f2f2f2;
    --divider: #6a6a6a;
    --lawn: #3f5a2c;
    --lawn-light: #6f8f4a;
    --sky: #6fa3d8;
    --sand: #c9a57c;
    --sand-light: #dcc2a0;
  }
  * { box-sizing: border-box; margin: 0; padding: 0; }
  html, body { width: 1200px; height: 784px; overflow: hidden; }
  body {
    background: var(--bg);
    font-family: "Questrial", "Century Gothic", sans-serif;
    display: flex;
    align-items: center;
    justify-content: center;
    gap: 40px;
  }
  .card {
    width: 560px;
    height: 320px;
    position: relative;
    overflow: hidden;
    box-shadow: 0 6px 18px rgba(0,0,0,.18);
  }

  /* Front: details */
  .card--front { background: var(--card-white); }
  .front__brand {
    position: absolute; top: 0; left: 0; right: 0; height: 168px;
    display: flex; align-items: center; justify-content: center;
  }
  .brand-name {
    font-size: 48px;
    color: var(--ink);
    letter-spacing: 1px;
  }
  .front__band {
    position: absolute; left: 0; right: 0; top: 168px; height: 10px;
    background: var(--teal);
  }
  .front__details {
    position: absolute; left: 0; right: 0; top: 178px; bottom: 0;
    background: var(--card-black);
  }
  .details__pattern {
    position: absolute; inset: 0;
    background: radial-gradient(ellipse at 70% 60%, var(--pattern-mid), var(--pattern-dark) 55%, var(--card-black));
  }
  .details__name {
    position: absolute; left: 28px; top: 58px;
    color: var(--teal); font-size: 22px;
  }
  .details__divider {
    position: absolute; left: 196px; top: 20px; bottom: 20px;
    width: 1px; background: var(--divider);
  }
  .contact-list {
    position: absolute; left: 212px; top: 20px;
    list-style: none; color: var(--text-light);
    font-size: 14.5px; line-height: 24px;
  }
  .contact-list li { display: flex; align-items: center; gap: 8px; white-space: nowrap; }
  .contact-list svg { width: 15px; height: 15px; flex: none; }

  /* Back: ceremony photos */
  .card--back { background: var(--sand); }
  .back__photos { position: absolute; inset: 0; width: 100%; height: 100%; }
  .back__brand {
    position: absolute; right: 40px; top: 168px;
    font-size: 30px; color: var(--ink);
  }
</style>
</head>
<body>

  <section class="card card--back">
    <svg class="back__photos" viewBox="0 0 560 320" aria-hidden="false">
      <defs>
        <linearGradient id="garden" x1="0" y1="0" x2="0" y2="1">
          <stop offset="0" stop-color="var(--sky)"/>
          <stop offset=".35" stop-color="var(--lawn-light)"/>
          <stop offset="1" stop-color="var(--lawn)"/>
        </linearGradient>
        <linearGradient id="beach" x1="0" y1="0" x2="0" y2="1">
          <stop offset="0" stop-color="var(--sky)"/>
          <stop offset=".25" stop-color="var(--sand-light)"/>
          <stop offset="1" stop-color="var(--sand)"/>
        </linearGradient>
      </defs>
      <rect role="img" aria-label="Beach wedding ceremony with white chairs on the sand" x="0" y="0" width="560" height="320" fill="url(#beach)"/>
      <path role="img" aria-label="Garden wedding ceremony with white aisle runner and harbour view" d="M0 0 H300 C230 70 200 200 230 320 H0 Z" fill="url(#garden)"/>
    </svg>
    <div class="back__brand">Vow Outfitters</div>
  </section>

  <section class="card card--front">
    <div class="front__brand"><span class="brand-name">Vow Outfitters</span></div>
    <div class="front__band"></div>
    <div class="front__details">
      <div class="details__pattern" role="img" aria-label="Dark swirl damask pattern"></div>
      <p class="details__name">Merel Thorpe</p>
      <div class="details__divider"></div>
      <ul class="contact-list">
        <li>
          <svg viewBox="0 0 16 16"><path d="M3.5 1.5l2.5 2.5-1.5 2a8 8 0 0 0 5.5 5.5l2-1.5 2.5 2.5-2 2C7 14 2 9 1.5 3.5z" fill="var(--text-light)"/></svg>
          0491 870 264
        </li>
        <li>
          <svg viewBox="0 0 16 16"><rect x="1.5" y="3.5" width="13" height="9" fill="none" stroke="var(--text-light)" stroke-width="1.4"/><path d="M1.5 3.5L8 9l6.5-5.5" fill="none" stroke="var(--text-light)" stroke-width="1.4"/></svg>
          vowoutfitters@mailbox-example.com
        </li>
        <li>
          <svg viewBox="0 0 16 16"><circle cx="8" cy="8" r="6.5" fill="none" stroke="var(--text-light)" stroke-width="1.3"/><ellipse cx="8" cy="8" rx="3" ry="6.5" fill="none" stroke="var(--text-light)" stroke-width="1.1"/><path d="M1.5 8h13" stroke="var(--text-light)" stroke-width="1.1"/></svg>
          www.vowoutfitters-example.com.au
        </li>
        <li>
          <svg viewBox="0 0 16 16"><rect x="2" y="2" width="12" height="12" fill="var(--text-light)"/></svg>
          VowOutfitters
        </li>
      </ul>
    </div>
  </section>

</body>
</html>
```